Business Card for Consulting Company

I would need a business card for my consulting company - the company brand and logos are defined and shared as part of this project. The proposed design for the business card can be reused as inspiration for my email signature.

```html
<!DOCTYPE html>
<html lang="en">
<head>
<meta charset="utf-8">
<title>Kelvane Advisory – Business Card</title>
<link rel="stylesheet" href="https://fonts.googleapis.com/css2?family=Exo+2:wght@500;600&family=Arimo:wght@400&display=swap">
<style>
  :root {
    --backdrop: #2b2b2d;
    --card: #1b1c1e;
    --teal: #1aa9ab;
    --white: #f2f2f2;
    --rule: #8a8a8a;
    --pattern-light: #3a3b3e;
    --pattern-dark: #141516;
  }
  * { margin: 0; padding: 0; box-sizing: border-box; }
  html, body { width: 1200px; height: 1108px; overflow: hidden; }
  body {
    background: var(--backdrop);
    position: relative;
    font-family: "Arimo", Arial, sans-serif;
  }
  .card {
    position: absolute;
    top: 204px;
    width: 420px;
    height: 700px;
    background: var(--card);
    border-radius: 22px;
    overflow: hidden;
  }
  .card--front { left: 150px; }
  .card--back { left: 630px; }

  .wordmark {
    position: absolute;
    top: 170px;
    left: 0;
    right: 0;
    display: flex;
    align-items: center;
    justify-content: center;
    gap: 14px;
    font-family: "Exo 2", sans-serif;
    font-weight: 600;
    font-size: 44px;
    color: var(--teal);
    letter-spacing: 1px;
  }
  .wordmark__dot {
    width: 22px; height: 22px;
    border-radius: 50%;
    background: var(--white);
  }
  .wordmark__sub {
    position: absolute;
    top: 232px; left: 0; right: 0;
    text-align: center;
    font-family: "Exo 2", sans-serif;
    font-weight: 600;
    font-size: 26px;
    color: var(--teal);
    letter-spacing: 2px;
  }

  .person {
    position: absolute;
    top: 410px; left: 0; right: 0;
    text-align: center;
  }
  .person__name {
    font-family: "Exo 2", sans-serif;
    font-weight: 500;
    font-size: 30px;
    color: var(--white);
  }
  .person__surname { color: var(--teal); }
  .person__role {
    margin-top: 6px;
    font-size: 19px;
    color: var(--white);
  }

  .contact-icons {
    position: absolute;
    top: 500px; left: 40px; right: 40px;
    display: flex;
    align-items: center;
    gap: 10px;
  }
  .contact-icons__rule { flex: 1; height: 1px; background: var(--rule); }
  .contact-icons svg { width: 30px; height: 30px; display: block; }

  .contact {
    position: absolute;
    top: 556px; left: 0; right: 0;
    text-align: center;
    font-size: 20px;
    line-height: 32px;
    color: var(--white);
  }
  .contact__accent { color: var(--teal); }

  .pattern {
    position: absolute;
    inset: 0;
    background: linear-gradient(135deg, var(--pattern-light) 0%, var(--card) 45%, var(--pattern-dark) 100%);
  }
  .back-mark {
    position: absolute;
    top: 470px; left: 0; right: 0;
    display: flex;
    align-items: center;
    justify-content: center;
    gap: 8px;
    font-family: "Exo 2", sans-serif;
    font-weight: 600;
    font-size: 30px;
    color: var(--teal);
  }
  .back-mark .wordmark__dot { width: 14px; height: 14px; }
</style>
</head>
<body>
  <section class="card card--front" aria-label="Card front">
    <div class="wordmark"><span>Kelvane</span><span class="wordmark__dot"></span></div>
    <div class="wordmark__sub">Advisory</div>

    <div class="person">
      <div class="person__name">Maren <span class="person__surname">Osterby</span></div>
      <div class="person__role">Founder &amp; CEO</div>
    </div>

    <div class="contact-icons">
      <span class="contact-icons__rule"></span>
      <svg viewBox="0 0 30 30" aria-label="Phone">
        <rect width="30" height="30" rx="5" fill="#1aa9ab"/>
        <path d="M8 11c0-2 2-3 7-3s7 1 7 3v2h-4v-2h-6v2H8z M10 14h10l2 8H8z" fill="#1b1c1e"/>
      </svg>
      <svg viewBox="0 0 30 30" aria-label="Email">
        <rect width="30" height="30" rx="5" fill="#1aa9ab"/>
        <rect x="7" y="9" width="16" height="12" fill="none" stroke="#1b1c1e" stroke-width="2"/>
        <path d="M7 9l8 7 8-7M7 21l6-5M23 21l-6-5" fill="none" stroke="#1b1c1e" stroke-width="1.6"/>
      </svg>
      <svg viewBox="0 0 30 30" aria-label="Website">
        <rect width="30" height="30" rx="5" fill="#1aa9ab"/>
        <circle cx="15" cy="15" r="8" fill="none" stroke="#1b1c1e" stroke-width="2"/>
        <path d="M7 15h16M15 7c-4 4-4 12 0 16M15 7c4 4 4 12 0 16" fill="none" stroke="#1b1c1e" stroke-width="1.4"/>
      </svg>
      <span class="contact-icons__rule"></span>
    </div>

    <div class="contact">
      <div>041-555 210 384</div>
      <div>hello@kelvane.com</div>
      <div>www.<span class="contact__accent">kelvaneadvisory</span>.com</div>
    </div>
  </section>

  <section class="card card--back" aria-label="Card back">
    <div class="pattern" role="img" aria-label="Tonal repeating brand-name pattern in glossy black on matte black"></div>
    <div class="back-mark"><span>Kelvane</span><span class="wordmark__dot"></span></div>
  </section>
</body>
</html>
```